Slogan as represent the company name: zyphorant

we look for a slogan which represent our company name, zyphorant.
Zyphorant specializes in microscopy based imaging solutions. sites: [login to view URL] and [login to view URL]
the slogan sentence should be composed of the company name letters (Z.Y.P.H.O.R.A.N.T) like TEMUKO: All day i dream about sex/sleep!
alternatively one can make sentences to use the initials for the company banner, like below:
B: beautiful images are our goal
I: image is life
O:
I: Illumination is light as a gift of love.
M: Micro and nano precision
A: Advertisements with beautiful images & beautiful words.
G: Great performance per price products
E: Ergonomical designed microscopes
R: Resolution one is....

```html
<!DOCTYPE html>
<html lang="en">
<head>
<meta charset="utf-8">
<title>Zyphorant Slogan Banner</title>
<link rel="stylesheet" href="https://fonts.googleapis.com/css2?family=Arimo:wght@400;700&family=Noto+Serif:wght@700;900&display=swap">
<style>
  :root {
    --ink-white: #ffffff;
    --tagline-coral: #f3857d;
    --deep-navy: #07122b;
    --mid-blue: #1d3f78;
    --light-blue: #5b8fcf;
    --glow: #b9d4f5;
  }
  html, body {
    margin: 0;
    padding: 0;
    overflow: hidden;
    background: var(--deep-navy);
  }
  .banner {
    position: relative;
    width: 1200px;
    height: 857px;
    overflow: hidden;
    font-family: "Arimo", Arial, sans-serif;
  }
  .lab-scene {
    position: absolute;
    inset: 0;
    background:
      radial-gradient(ellipse 260px 120px at 560px 720px, rgba(185,212,245,0.55), transparent 70%),
      radial-gradient(ellipse 520px 420px at 900px 300px, rgba(91,143,207,0.55), transparent 75%),
      radial-gradient(ellipse 480px 520px at 420px 300px, rgba(40,70,120,0.7), transparent 75%),
      linear-gradient(160deg, var(--mid-blue) 0%, #12285a 45%, var(--deep-navy) 100%);
  }
  .acrostic {
    position: absolute;
    left: 24px;
    top: 18px;
    margin: 0;
    padding: 0;
    list-style: none;
    color: var(--ink-white);
    font-size: 57px;
    line-height: 92px;
    letter-spacing: 0.5px;
  }
  .acrostic li { white-space: nowrap; }
  .acrostic .initial { font-weight: 700; }
  .brand-block {
    position: absolute;
    left: 520px;
    top: 520px;
    width: 680px;
    transform: rotate(-15deg);
    transform-origin: center;
    text-align: center;
  }
  .brand-name {
    margin: 0;
    font-family: "Noto Serif", Georgia, serif;
    font-weight: 900;
    font-size: 96px;
    letter-spacing: 2px;
    color: var(--ink-white);
    line-height: 1;
  }
  .brand-tagline {
    margin: 14px 0 0 70px;
    width: 360px;
    font-family: "Noto Serif", Georgia, serif;
    font-weight: 700;
    font-size: 28px;
    line-height: 33px;
    color: var(--tagline-coral);
  }
</style>
</head>
<body>
<div class="banner">
  <div class="lab-scene" role="img" aria-label="Close-up photograph of a laboratory microscope with objective lenses over a lit glass slide, in dark blue tones"></div>

  <ul class="acrostic">
    <li><span class="initial">Z</span>ooming</li>
    <li><span class="initial">Y</span>ields</li>
    <li><span class="initial">P</span>erfect</li>
    <li><span class="initial">H</span>igh-resolution</li>
    <li><span class="initial">O</span>ptics</li>
    <li><span class="initial">R</span>evealing</li>
    <li><span class="initial">A</span>lways</li>
    <li><span class="initial">N</span>ew</li>
    <li><span class="initial">T</span>ruths</li>
  </ul>

  <div class="brand-block">
    <h1 class="brand-name">ZYPHORANT</h1>
    <p class="brand-tagline">Zooming yields perfect optics revealing new truths!</p>
  </div>
</div>
</body>
</html>
```